Marine Business Card

We install Lighting, Sound, Video, PA Systems to hotels, nightclubs, Restaurants, Cruise Ships.

Target Market(s)

We want to focus on the Marine or Maritime/Cruise industry. Passenger ships and cruise liners are the companies we want to appeal to

Industry/Entity Type

Business

Contact Information for Business Card

Alden Marwick
Managing Director
Harbourne Vista Audio Marine Ltd

Requirements
Must have
• Office: 01632 960482
Mobile: 07700 900317
alden@harbournevistaaudio.co.uk
www.harbournevistaaudio.co.uk

```html
<!DOCTYPE html>
<html lang="en">
<head>
<meta charset="utf-8">
<title>Harbourne Vista Audio Marine Ltd – Business Card</title>
<link href="https://fonts.googleapis.com/css2?family=Open+Sans:wght@300;400;600;700&display=swap" rel="stylesheet">
<style>
  :root {
    --page: #ffffff;
    --card: #1f1f21;
    --card-light: #262629;
    --accent: #2a79c0;
    --disc: #f3f6f9;
    --text-strong: #ffffff;
    --text-soft: #c9c9cc;
    --text-muted: #a3a3a8;
  }
  * { margin: 0; padding: 0; box-sizing: border-box; }
  html, body {
    width: 1200px; height: 1056px; overflow: hidden;
    background: var(--page);
    font-family: "Open Sans", sans-serif;
  }
  .stage { position: relative; width: 1200px; height: 1056px; }
  .card {
    position: absolute; left: 343px; width: 514px; height: 331px;
    background: linear-gradient(160deg, var(--card-light) 0%, var(--card) 55%, #1c1c1e 100%);
    box-shadow: 0 2px 8px rgba(0,0,0,0.18);
    overflow: hidden;
  }
  .card--front { top: 163px; }
  .card--back { top: 557px; }

  .accent-tab { position: absolute; background: var(--accent); }
  .card--front .accent-tab { right: 0; top: 149px; width: 10px; height: 41px; }
  .card--back .accent-tab { left: 0; top: 58px; width: 9px; height: 45px; }

  .brand-disc {
    position: absolute; left: 31px; top: 94px;
    width: 140px; height: 140px; border-radius: 50%;
    background: var(--accent);
  }
  .company {
    position: absolute; right: 38px; top: 145px; text-align: right;
    color: var(--text-strong);
  }
  .company__name { font-size: 15.5px; font-weight: 600; line-height: 20px; }
  .company__tagline { font-size: 10.3px; color: var(--text-soft); line-height: 15px; margin-top: 1px; letter-spacing: -0.1px; }

  .person { position: absolute; left: 31px; top: 50px; }
  .person__name { font-size: 25px; font-weight: 300; color: var(--text-strong); line-height: 34px; }
  .person__role { font-size: 10.5px; color: var(--text-muted); line-height: 11px; margin-top: -1px; }

  .contacts { position: absolute; left: 31px; top: 228px; list-style: none; }
  .contacts li { font-size: 12.5px; line-height: 17.3px; color: var(--text-strong); white-space: nowrap; }
  .contacts .label { color: var(--text-soft); margin-right: 4px; }

  .big-disc {
    position: absolute; left: 327px; top: 151px;
    width: 240px; height: 240px; border-radius: 50%;
    background: var(--disc);
  }
</style>
</head>
<body>
<div class="stage">
  <section class="card card--front">
    <div class="brand-disc"></div>
    <div class="company">
      <div class="company__name">Harbourne Vista Audio Marine Ltd</div>
      <div class="company__tagline">We specialize in Lighting, Sound, Video,PA Systems<br>to hotels, nightclubs, Restaurants, Cruise Ships</div>
    </div>
    <div class="accent-tab"></div>
  </section>

  <section class="card card--back">
    <div class="accent-tab"></div>
    <div class="person">
      <div class="person__name">Alden Marwick</div>
      <div class="person__role">Managing Director<br>Harbourne Vista Audio Marine Ltd</div>
    </div>
    <ul class="contacts">
      <li><span class="label">Office:</span> 01632 960482</li>
      <li><span class="label">Mobile:</span> 07700 900317</li>
      <li><span class="label">Email:</span> alden@harbournevistaaudio.co.uk</li>
      <li><span class="label">Websie:</span> www.harbournevistaaudio.co.uk</li>
    </ul>
    <div class="big-disc"></div>
  </section>
</div>
</body>
</html>
```